Jewellery Store Web design

We are looking at a redesign of an exclusive jewellery store. The idea of what we want is to display the type of jewellery we sell. Our main product range is white diamonds. We do not want people to buy online. This site will not display any prices but only display photos and the information about the store.
The client believes in the saying “A picture makes a thousand words” so this site needs to be more pictures – less words.
The website that the client loves is:
www.pelwickgems.com
The existing site can be found at:
http://www.lumarothevaults.com.au/
The site cannot be written in flash as the site must be viewable on Vexa/Talvo devices and will be implemented with our already designed CMS.
This project is only for the PSD file. We will code up the final submission ourselves.
Updates
Reason: We have some great designs and we have decided to gurrantee the project and for those who want a payment gurrantee to enter.
Target Market(s)
Young Couples, 30+
Industry/Entity Type
Store
Look and feel
Each slider illustrates characteristics of the customer's brand and the style your logo design should communicate.

```html
<!DOCTYPE html>
<html lang="en">
<head>
<meta charset="utf-8">
<title>Lumaro The Vaults</title>
<link rel="stylesheet" href="https://fonts.googleapis.com/css2?family=Didact+Gothic&family=Cinzel:wght@400&display=swap">
<style>
  :root {
    --page-bg: #222222;
    --nav-bg: #ffffff;
    --nav-text: #6e6e6e;
    --nav-active: #333333;
    --logo-text: #ffffff;
    --body-text: #9a9a9a;
    --footer-text: #d8d8d8;
    --photo-light: #f4f2f3;
    --photo-mid: #dcd8dc;
    --arrow-ring: #3a3a3a;
    --arrow-fill: #262626;
  }
  * { margin: 0; padding: 0; box-sizing: border-box; }
  html, body { width: 1200px; height: 716px; overflow: hidden; }
  body {
    position: relative;
    background: var(--page-bg);
    font-family: "Didact Gothic", "Century Gothic", sans-serif;
  }
  .stage-glow {
    position: absolute;
    left: 140px; top: 110px;
    width: 920px; height: 500px;
    background: radial-gradient(ellipse at center, rgba(255,255,255,0.85) 0%, rgba(200,200,200,0.55) 35%, rgba(80,80,80,0.2) 62%, rgba(34,34,34,0) 75%);
  }
  .main-nav {
    position: absolute;
    left: 88px; top: 0;
    width: 1025px; height: 40px;
    background: var(--nav-bg);
  }
  .main-nav ul { list-style: none; }
  .main-nav li {
    position: absolute;
    top: 12px;
    font-size: 14px;
    letter-spacing: 0.2px;
    color: var(--nav-text);
    text-transform: uppercase;
  }
  .main-nav li.is-active {
    color: var(--nav-active);
    text-decoration: underline;
    text-underline-offset: 3px;
  }
  .nav-marker { position: absolute; left: 50px; top: 35px; }
  .brand {
    position: absolute;
    left: 0; top: 76px;
    width: 1200px;
    text-align: center;
    color: var(--logo-text);
    font-family: "Cinzel", "Times New Roman", serif;
    font-weight: 400;
  }
  .brand-name { display: block; font-size: 46px; line-height: 54px; letter-spacing: 1px; }
  .brand-sub { display: block; font-size: 14px; line-height: 22px; letter-spacing: 1px; }
  .hero-photo {
    position: absolute;
    left: 262px; top: 190px;
    width: 676px; height: 326px;
    background: linear-gradient(160deg, var(--photo-light) 0%, var(--photo-mid) 55%, #ece9ec 100%);
  }
  .slider-arrow { position: absolute; top: 332px; }
  .slider-arrow.prev { left: 176px; }
  .slider-arrow.next { left: 975px; }
  .intro {
    position: absolute;
    left: 122px; top: 555px;
    width: 949px;
    font-size: 12.4px;
    line-height: 18px;
    color: var(--body-text);
    text-align: justify;
  }
  .copyright {
    position: absolute;
    left: 88px; top: 682px;
    font-size: 11px;
    color: var(--footer-text);
  }
</style>
</head>
<body>
  <div class="stage-glow"></div>

  <nav class="main-nav">
    <ul>
      <li class="is-active" style="left:34px">Home</li>
      <li style="left:184px">About Us</li>
      <li style="left:355px">Collection</li>
      <li style="left:552px">Diamonds</li>
      <li style="left:742px">Friends</li>
      <li style="left:914px">Contact</li>
    </ul>
    <svg class="nav-marker" width="10" height="6" viewBox="0 0 10 6" aria-hidden="true">
      <polygon points="5,0 10,6 0,6" fill="#222222"/>
    </svg>
  </nav>

  <header class="brand">
    <span class="brand-name">LUMARO</span>
    <span class="brand-sub">THE VAULTS</span>
  </header>

  <div class="hero-photo" role="img" aria-label="Close-up photograph of a pearl bracelet with silver spacers and pink gemstone settings"></div>

  <svg class="slider-arrow prev" width="42" height="42" viewBox="0 0 42 42" aria-label="Previous slide">
    <circle cx="21" cy="21" r="20" fill="var(--arrow-fill)" stroke="var(--arrow-ring)" stroke-width="1.5"/>
    <polyline points="22.5,18 19.5,21 22.5,24" fill="none" stroke="#cccccc" stroke-width="1.2"/>
  </svg>
  <svg class="slider-arrow next" width="42" height="42" viewBox="0 0 42 42" aria-label="Next slide">
    <circle cx="21" cy="21" r="20" fill="var(--arrow-fill)" stroke="var(--arrow-ring)" stroke-width="1.5"/>
    <polyline points="19.5,18 22.5,21 19.5,24" fill="none" stroke="#cccccc" stroke-width="1.2"/>
  </svg>

  <p class="intro">Lumaro The Vaults is Eastvale's most recent jewellery boutique to open on Marlow Street, Eastvale WA specialising in rare diamonds and pearls jewellery. With an in-house designer, a team of qualified jewellers and setters located on the premises, Lumaro The Vaults design exclusive individual pieces, engagement and weding rings. Lumaro The Vaults's quality pieces are everlasting and will be cherished beyond a life time. Visit Lumaro The Vaults if you would like to enquire about their diamond selection or in-house design service.</p>

  <footer class="copyright">&copy; 2012. All Rights Reserved.</footer>
</body>
</html>
```